High end, luxury real estate property brochure

I need to have a property Brochure with 10-15 pages that will allow me to enter 30-40 photos and content about the home. It needs to be very high end and able to be edited in either word or publisher. I want to be able to use the pages individually when appropriate and then all together for larger homes. I need the template back by early Wednesday morning. Ideally, the brochure will be like a small booklet with a place for photos and content on the front and back of the pages. I need to add my company's logo and my photo to the project along with our office address etc..
Updates

Project Deadline Extended
Reason: I have decided to purchase more than one design and want to extend time for additional submissions.

Target Market(s)

Home Buyers in the Midwest (Indiana)

Industry/Entity Type

Real Estate Agent

Font styles to use
Serif

Requirements
Must have
• Graphically appealing. Integrated look between the pages. Several places for me to add photos of different sizes to highlight the homes features. The ability for me to change font, font colors, background colors, etc... Must have a high end, luxury feel. I will be adding descriptions and content about the photos so I need areas to add that information. I want the project to be able to be printed as a booklet for larger homes and to be able to use parts of the brochure for smaller homes as I won't have as many photos. Resolution must be fantastic. Clean lines.
Nice to have
• I am with Brantford Osgood Realty and our colors our logo is red so many of our publications are in Black and red. Dorian Fairbrook Promo Studios is a program that has some high end marketing pieces and designs that I like. I prefer the designs in the slate and black colors.
Should not have
• Cartoons graphics, pastel colors, "busy" designs.

```html
<!DOCTYPE html>
<html lang="en">
<head>
<meta charset="utf-8">
<title>Luxury Property Brochure – Spreads</title>
<link href="https://fonts.googleapis.com/css2?family=Roboto+Slab:wght@700&family=Lora:ital@1&family=Arimo:wght@400&display=swap" rel="stylesheet">
<style>
:root{
  --brand-red:#b3151b;
  --ink:#1f1f1f;
  --body:#2b2b2b;
  --paper:#ffffff;
  --backdrop:#d6d6d6;
  --tab-black:#1a1a1a;
}
*{margin:0;padding:0;box-sizing:border-box}
html,body{width:857px;height:1200px;overflow:hidden;background:var(--backdrop)}
.canvas{position:relative;width:857px;height:1200px}
.spread{position:absolute;left:45px;width:773px;height:499px;background:var(--paper);overflow:hidden}
.spread--one{top:53px}
.spread--two{top:653px}
.gutter{position:absolute;left:386px;top:0;width:1px;height:100%;background:#e2e2e2}
.abs{position:absolute}
.photo{position:absolute}
.framed{border:2px solid var(--brand-red)}
.body-text{font-family:"Arimo",Arial,sans-serif;font-size:6.1px;line-height:9.4px;color:var(--body)}
.body-text p{margin-bottom:6px}
.col{position:absolute;overflow:hidden}
.subhead{font-family:"Roboto Slab",Georgia,serif;font-weight:700;color:var(--brand-red);font-size:7.4px;margin:2px 0 5px}
.headline{font-family:"Roboto Slab",Georgia,serif;font-weight:700;color:var(--brand-red);font-size:10.4px;line-height:13.6px;margin-bottom:30px}
.page-tab{position:absolute;top:0;height:35px;background:var(--paper);font-family:"Roboto Slab",Georgia,serif;font-weight:700;color:var(--brand-red);font-size:7px;display:flex;align-items:center;justify-content:center}
.text-panel{position:absolute;left:27px;top:54px;width:161px;height:426px;background:rgba(255,255,255,.86);padding:17px 9px 0 9px}
.pull-quote{position:absolute;left:225px;top:219px;width:132px;border-left:3px solid var(--brand-red);padding-left:10px;font-family:"Lora",Georgia,serif;font-style:italic;font-size:6.9px;line-height:10.6px;color:#23324a}
.folio{position:absolute;top:0;height:35px;width:30px;background:var(--tab-black);color:#fff;font-family:"Arimo",Arial,sans-serif;font-size:7px;display:flex;align-items:center;justify-content:center}
.section-band{position:absolute;top:0;height:35px;background:var(--brand-red);color:#fff;font-family:"Roboto Slab",Georgia,serif;font-weight:700;font-size:6.8px;display:flex;align-items:center;padding:0 8px}
.photo-caption{position:absolute;background:var(--brand-red);color:#fff;font-family:"Lora",Georgia,serif;font-style:italic;font-size:6.3px;line-height:10px;padding:6px 7px}
</style>
</head>
<body>
<main class="canvas">

  <!-- Spread: pages 8–9 -->
  <section class="spread spread--one">
    <div class="photo" role="img" aria-label="Family pulling a paper house on a rope into a starry blue sky" style="left:0;top:0;width:387px;height:499px;background:linear-gradient(180deg,#1b3f7c 0%,#3f78b8 40%,#9cc3e3 75%,#e8eef3 100%)"></div>
    <div class="page-tab" style="left:0;width:27px">8</div>

    <div class="text-panel body-text">
      <h2 class="headline">Wipsus provit pora si sin nobis ad mo ipsae. Unt veliam</h2>
      <p>Perundi rem faceper ecuscil ssumquis dic to ius dolorem ea voluptature lam ium laut aut aut qui re pra sitas volorumque sitem a dit et veliquae nihicimpore erum, volestia sandelit veles ilis derrore dolorum laccuscipsum quatis inumet mi, am sima nat.</p>
      <h3 class="subhead">Optati iliquis delendu ciminus.</h3>
      <p>Metur, te eosande mquatur serae. Itateni mporiae in et eatet abore, nobis este nectumque sum que lant. Lum et omnis ex este videstes voluptis si blabore iciist modia volorissus.</p>
      <p>Si nissi iditas aliquiae voluptibus el maximagnam rest, sunt dolent molorei cilitat et, sintis elendam laccatemqui doluptae. Pid earumqu iatust accatem quidebit assequi ommolupture etus doluptatum vel illam, solorem harum que preprae poreium que pa sitaqui coribus.</p>
      <h3 class="subhead">Ehendun dandendae doluptatat</h3>
      <p>Nemporrorrum esto est eos anihit, consecute quae iuntiss itatasit, sa neculabo. Itatio mi, quatia eatur restia voluptate peles mod que prorpor alit eatemporem. Ut ullab ipsae nobisi officid moles aut rerovid quat dolore pero ipici dolorum eum faccumquam que dus nonsers peribus ent.</p>
      <p>Um excearcit ut ea dolo volutaturia voluptatia aut prores res alitinc idesequia vent, videbit a sument aut aut la doluptis aut am reprovidebit quiam qui aut quam que int fugia cus eum enienem volestis dolores ad mo berehen.</p>
    </div>

    <blockquote class="pull-quote">Andigend isquas sunto mod que eos volorem olorrovit quissit, nati consequam que providi totatum fugiam rendi inctaecepres diae. Itasi officiis laces eume accae.</blockquote>

    <div class="gutter"></div>

    <div class="photo" role="img" aria-label="Three-storey timber and stone luxury home with landscaped front garden" style="left:387px;top:0;width:386px;height:243px;background:linear-gradient(180deg,#8fb1d4 0%,#c9d7e2 30%,#8a6a4a 55%,#4f6a33 80%,#6f7a5c 100%)"></div>
    <div class="page-tab" style="left:745px;width:28px">9</div>
    <div class="photo framed" role="img" aria-label="Dining room with long table, upholstered chairs and chandelier" style="left:595px;top:216px;width:150px;height:123px;background:linear-gradient(160deg,#d8d2c8 0%,#a8998a 50%,#4a3a30 100%)"></div>

    <div class="col body-text" style="left:414px;top:271px;width:158px;height:220px">
      <p>Fugiaeri orecepu diostot atessi voluptae maiores ectatemporem vellut ipsunti atureseque inctem ut et aperiberio conserferia num enimpor as dolumquas as ut maioraecte officiatque net autatem rest, qui il eaquam et ese endebis as destiost rem niendendione qui vernam, occatistius, sam, eatem untio es inis eos pediorum reius estia pa pre consequam vendae sim et acerio beremporio. Itas nonse pra voluptis rem ut optatur?</p>
      <h3 class="subhead">Temporr ovitae quibus voluptatur</h3>
      <p>Saniminust alit, que earciamusam, odit optium iduciurita conseque ium quis everis con placcuptat des eatiam, omnit ut voluptatquia nus ea enimusa nitatem restibusdae doluptius.</p>
      <p>Apici que solum re plique placcab orepro testium expe cuptaquias plibus et endigni mollant, optatiur sit et et lam que explabo reptassit alit ut rerchil id quam, commo blam fugias et eum doluptatem voluptium evellibus, utecte lab imento eum que porestr uptatioriam et hil molorep udigenistem</p>
    </div>
    <div class="col body-text" style="left:594px;top:355px;width:154px;height:140px">
      <p>doloruptat volore dessimporem quo optae eum fuga. Ut providi tem re volorio nsequam aborum eum ad mil mos volore voluptat.</p>
      <p>Sed quati tenim faceria ntibus, ut omnis maximperem. Nam, sed eaquam ima dolori ullabo. Apeliatum consedi sinihit volorerro mod ut lautatu ribust quiatis ant ut dolore experia dolupta evelest rumquodi ut dolore volection premquo dipsum vel iliquis quo moditis dolut prae maximinctur, ommolorem adis aut utem asi te et illautendae. Optaspe liatem volenisciimo eveliquatia nonseni hicipsam idestis ipsapid maio veruptibero velluptae nem facipientur?</p>
    </div>
  </section>

  <!-- Spread: pages 10–11 -->
  <section class="spread spread--two">
    <div class="folio" style="left:0">10</div>
    <div class="section-band" style="left:30px;width:101px">Qsusuis everum</div>

    <div class="col body-text" style="left:27px;top:51px;width:146px;height:110px">
      <p>Agnatur, id et accaturitas ad molorep erferum ad elit eiume sunto qui amus, sunt, ommoluptatio ius nimus.</p>
      <p>Expedit aut omnis adit a none etus as ea pedit, ullupta temolor erumentempor aspero que labo. Liciati oreperehento mintiaturi verferunt.</p>
      <p>Ro mod esequos at. Event apel ipieni apit, tem eatios am solorum simus invelitium re voloremquos eic temporepe con ento odit mint</p>
    </div>
    <div class="col body-text" style="left:207px;top:51px;width:152px;height:200px">
      <p>aspernam, volorios repudig enisciis erfercil eaquam que voluptam rerumque non et venihil molor solorehenda ducit, simustiossum re, unt porempe perovid elignimpero int quosa dolore, coressunt occat dolectis reptas essimet que volupit volorec esciend aecaboribus rehenis apedia qui optissunt aut exeria dolenissimet eatur aute voluptatur acepra dolupta temporibus et des dolupit, inim facitius mintur, officiunt laboriaest ea vitem incia dolupta excerna tibus.</p>
      <p>Metur, acimoluptis rerum, nem rem quisquasint faceaquis ipsam sed moluptur audaepuda cusa quo eatin rest etus.</p>
      <p>Evelese quatis ea issiti as volo molorem quis et asperuptatis aut aut veritatiis cusdae que pore non cum veliqui autas niscia et et plam ius esto eium quost remporio. Faces esciendi cone naturerumqui tetur modic tem non num quates pelest od qui</p>
    </div>

    <div class="photo" role="img" aria-label="Two-storey house at dusk with lit double garage and flower beds" style="left:0;top:253px;width:515px;height:246px;background:linear-gradient(180deg,#1c2d6e 0%,#3a4f98 35%,#c7c2b8 60%,#6a5a52 80%,#8a6a72 100%)"></div>
    <div class="photo framed" role="img" aria-label="Bathroom with freestanding tub, wall lamps and pedestal sink" style="left:22px;top:164px;width:166px;height:111px;background:linear-gradient(160deg,#e7cf94 0%,#b89468 50%,#6e5234 100%)"></div>

    <div class="gutter"></div>

    <div class="section-band" style="left:642px;width:103px;justify-content:flex-end">Otae veriame omnim</div>
    <div class="folio" style="left:745px;width:28px">11</div>

    <div class="photo" role="img" aria-label="Patio lounge with sofa and sunset view over the water" style="left:414px;top:54px;width:102px;height:138px;background:linear-gradient(180deg,#c9d3de 0%,#e1a46c 45%,#5e4a3c 75%,#2e2a28 100%)"></div>
    <div class="photo-caption" style="left:414px;top:192px;width:102px;height:44px">Ucimoluptis rerum, nem rem quisquasint faceaquis ipsam molu.</div>
    <div class="photo" role="img" aria-label="Stone and shingle family home with trimmed lawn and flower garden" style="left:529px;top:54px;width:218px;height:115px;background:linear-gradient(180deg,#8fb6e3 0%,#c8d9ea 30%,#6a5e55 55%,#4d7a2e 80%,#5f8f36 100%)"></div>

    <div class="col body-text" style="left:529px;top:185px;width:104px;height:300px">
      <p>Um faccus dit, aut ad ut ut enditam, quunt fugitecus esti ommodipsusam et asped etur si odio blaborro ipsae volor re consero commoluptur? Illit dus re coribus cum eum, ut mos dis ex et quatiosserro volum aditatur, officto voloris illistiatenda nis molore rehenis dolupta temquas quiditiatem sim volor re nonserita quae il ipsaeca ectorenis as exceptur arcium susantibus.</p>
      <p>Liquiatem etur? Pariasp ellabo. Nam et aute voloreius dem et di ducis ut es ad moloreped molorepudae volo tenimpos dollupta vella non rerit hitate nit rehenim illandic to con pro dollamusa dolest, se consed quodis nonsed quis nus, in nimporem alis sitatur iscipiciis essus eum, odit, quaescipsus.</p>
      <p>Fugit as doluptis utatia dem si inis maxim accatem porporehent, sus qui optio mod quaestis vendis dollupi ssequis nestempore porersped qui qui voluptaqui unt eos dollecepta nobitas dolore eaque dolo voluptae escia comnis ditatior acea sentist reriae</p>
    </div>
    <div class="col body-text" style="left:645px;top:185px;width:104px;height:300px">
      <p>doloribus molorehentio blabora vel experum fuga. Um ex et quis rerio quo moluptur sae odi viduci ad exerspelliam doluptur? Harumqui nos doluptate doluptatem qui dem laut rerchic idicium aut doluptatum dolum delibus unt, volendanda quo voluptam rem dolor aliquat re quo inullam aut quas sitature simporro in cor ad ma venestia volestempor reprepe rempori bernam vitiunt la que net voluption et aut eum que vid molorem porerfero ommoloribus molorio nseque asitate nis aut alis dolupta spidunt, nihilit aesedis nonsequae consequam, tem dolut dusaectem ipitibus dolupti usapiss itaessequiae nossini enimusciis mod eicaborum que eatinti isquae estis enimusam, quidero berupta quunt, sant voloris inimil exerores consequasit, sit, idipsap edigendel es dellorum quaecabor acilique culpa nis aliquatius maionet lab illacimossim cor a quaspie nissent fugit velitib usdamus eum aut dollandae maxime digende rsperum quid unt et acearum lab invella borporia corecer eratum la paribus volecab</p>
    </div>
  </section>

</main>
</body>
</html>
```